Tove & Lark Designs - Promotions flyer

I am a locally based Interior designer /stylist on Sydney's lower north shore. I would like to offer my services:
Full Professional Styling Services and Furniture Hire
Colour Consultation – Interior / exterior
Floor Coverings
Furniture selection and sourcing
Window Treatments
Wallpaper
Soft Furnishings
Upholstery
Renovations

I would like to offer a free consultation
Updates

Project Deadline Extended
Reason: I've been speaking with a designer and need her to make one more change. I have tried to message her twice, but have had no reply. Once she makes these changes I'm ready to sign off on the design. Thanks Harriet

Target Market(s)

30 - 60's middle to high income earners

Industry/Entity Type

Floor

Requirements
Must have
• one sided DL size
Use my logo
1 or 2 images of interior space or image of a lamp, cushion, lounge etc
The following contact details:
Mobile: 041 xxx xxxx
Website Address: www.tovelarkdesigns.example.au

```html
<!DOCTYPE html>
<html lang="en">
<head>
<meta charset="utf-8">
<title>Tove &amp; Lark Designs – Promotions Flyer</title>
<link rel="stylesheet" href="https://fonts.googleapis.com/css2?family=Arvo:wght@700&family=Roboto+Condensed:wght@400;700&display=swap">
<style>
  :root {
    --peach: #f7b99b;
    --peach-light: #fbd6c2;
    --orange: #ef6a26;
    --slate: #5f5f63;
    --white: #ffffff;
    --photo-light: #e9e5df;
    --photo-mid: #b9a894;
    --photo-dark: #2c2a28;
  }
  html, body {
    margin: 0;
    padding: 0;
    overflow: hidden;
    background: #ffffff;
  }
  .flyer {
    position: relative;
    width: 1200px;
    height: 572px;
    overflow: hidden;
    font-family: "Roboto Condensed", "Arial Narrow", sans-serif;
  }
  .interior-photo {
    position: absolute;
    left: 480px;
    top: 0;
    width: 720px;
    height: 572px;
    background:
      linear-gradient(180deg, rgba(0,0,0,0) 70%, rgba(30,28,26,0.85) 100%),
      linear-gradient(90deg, var(--photo-dark) 0%, var(--photo-light) 30%, #f4f2ee 60%, var(--photo-mid) 100%);
  }
  .peach-panel {
    position: absolute;
    left: 0;
    top: 0;
    width: 600px;
    height: 572px;
    background: linear-gradient(90deg, var(--peach-light) 0%, var(--peach) 78%, rgba(247,185,155,0) 100%);
  }
  .headline {
    position: absolute;
    left: 0;
    top: 18px;
    width: 530px;
    margin: 0;
    text-align: center;
    font-family: "Arvo", "Rockwell", serif;
    font-weight: 700;
    line-height: 0.98;
    color: var(--slate);
    font-size: 58px;
  }
  .headline .accent {
    color: var(--orange);
    font-size: 68px;
  }
  .services-title {
    position: absolute;
    left: 0;
    top: 388px;
    width: 530px;
    margin: 0;
    text-align: center;
    color: var(--white);
    font-weight: 700;
    font-size: 32px;
    line-height: 1;
  }
  .services-title .sub {
    display: block;
    font-weight: 400;
    font-size: 29px;
    margin-top: 4px;
  }
  .service-list {
    position: absolute;
    left: 14px;
    top: 462px;
    margin: 0;
    padding: 0;
    list-style: none;
    color: var(--white);
    font-size: 24px;
    line-height: 34px;
  }
  .service-list .dot {
    display: inline-block;
    width: 14px;
    height: 14px;
    border-radius: 50%;
    background: var(--orange);
    margin: 0 5px;
    vertical-align: 1px;
  }
  .brand-name {
    position: absolute;
    left: 560px;
    top: 482px;
    margin: 0;
    font-family: "Arvo", "Rockwell", serif;
    font-weight: 700;
    font-size: 30px;
    line-height: 1.05;
    color: var(--orange);
    text-align: center;
  }
  .contact {
    position: absolute;
    left: 795px;
    top: 510px;
    color: var(--white);
    font-size: 14px;
    line-height: 18px;
  }
  .contact strong { font-size: 17px; }
  .offer-badge {
    position: absolute;
    left: 1018px;
    top: 398px;
    width: 190px;
    height: 190px;
  }
</style>
</head>
<body>
<div class="flyer">
  <div class="interior-photo" role="img" aria-label="Photograph of a bright styled kitchen and dining area with timber table and cross-back chairs"></div>
  <div class="peach-panel"></div>

  <h1 class="headline">We Take<br><span class="accent">Space</span><br>and Make<br>It Your<br><span class="accent">Place</span> !</h1>

  <h2 class="services-title">Full Professional Styling<span class="sub">Services and Furniture Hire</span></h2>

  <ul class="service-list">
    <li>Colour Consultation – Interior/exterior<span class="dot"></span>Floor Coverings</li>
    <li>Furniture selection and sourcing<span class="dot"></span>Window Treatments</li>
    <li>Wallpaper<span class="dot"></span>Soft Furnishings<span class="dot"></span>Upholstery<span class="dot"></span>Renovations</li>
  </ul>

  <p class="brand-name">Tove &amp; Lark<br>designs</p>

  <div class="contact">
    <strong>Mobile: 041 xxx xxxx</strong><br>
    www.tovelarkdesigns.example.au
  </div>

  <svg class="offer-badge" viewBox="0 0 190 190" aria-label="Free consultation">
    <circle cx="95" cy="95" r="90" fill="#ef6a26"/>
    <circle cx="95" cy="95" r="72" fill="none" stroke="#ffffff" stroke-width="4"/>
    <text x="95" y="88" text-anchor="middle" fill="#ffffff" font-family="Roboto Condensed, sans-serif" font-weight="700" font-size="34">FREE</text>
    <text x="95" y="118" text-anchor="middle" fill="#ffffff" font-family="Roboto Condensed, sans-serif" font-weight="700" font-size="19">CONSULTATION</text>
  </svg>
</div>
</body>
</html>
```